Technical Redesign of AI-Generated Method & Topic Graphics for PowerPoint

e have a set of graphics and diagrams that were initially created using AI. The content, structure, and overall layout are already defined and should remain largely unchanged.

The objective is NOT to create completely new designs. This is primarily a technical refinement and conversion project. The graphics need to be professionally redrawn, cleaned up, and rebuilt so that they:

• Look less AI-generated and more professional/corporate
• Match our existing corporate website style
• Are fully editable in Microsoft PowerPoint
• Use consistent fonts, colors, spacing, and iconography
• Maintain the original meaning and information structure

REFERENCE WEBSITE
https://moorwald-forschung. at/

Please use the website as the primary reference for:
• Color palette
• Typography
• Visual language
• General corporate look and feel
• Professional, research-oriented appearance

The style should be clean, technical, modern, and suitable for a scientific/research institution.

SCOPE OF WORK
For each supplied graphic:

1. Recreate the graphic manually
- Do not simply trace or export the AI image.
- Rebuild all elements using PowerPoint native objects where possible.

2. Improve visual quality
- Remove typical AI-generated inconsistencies.
- Correct alignment, spacing, proportions, and visual hierarchy.
- Standardize icons and graphic elements.

3. Corporate style adaptation
- Apply colors and typography consistent with our website.
- Use a professional and technically oriented visual style.
- Avoid decorative or overly creative design elements.

4. Ensure full editability
- All text must remain editable.
- Shapes should be editable PowerPoint objects.
- Icons should preferably be vector-based.
- Elements should not be flattened into images unless absolutely necessary.

DELIVERABLES
Required output:

• Microsoft PowerPoint (.pptx)
• All graphics fully editable
• Layered and logically grouped objects
• Consistent formatting across all graphics
• Optional source files (.svg, .ai, or . eps) if available

DESIGN DIRECTION
Please focus on:

• Technical accuracy
• Professional presentation quality
• Corporate consistency
• PowerPoint usability

Please do NOT focus on:
• Creating alternative concepts
• Artistic reinterpretations
• Major layout changes
• Creative redesigns

The goal is to transform existing AI-generated diagrams into professional, corporate-standard, PowerPoint-editable graphics that fit seamlessly with the Moorwaldinstitut Graz website and presentation materials.

```html
<!DOCTYPE html>
<html lang="en">
<head>
<meta charset="utf-8">
<title>Integrated Process Assessment – Template Design Ideas</title>
<link rel="stylesheet" href="https://fonts.googleapis.com/css2?family=Archivo:wght@500;600;700;800&family=Open+Sans:wght@300;400;500;600;700&display=swap">
<style>
  :root{
    --green:#6c8a37;
    --green-dark:#56702a;
    --green-soft:#e0e5d6;
    --ink:#1d1d1b;
    --grey-text:#4f4f4f;
    --band:#d4d5d7;
    --line:#7a7a7a;
    --white:#ffffff;
  }
  *{margin:0;padding:0;box-sizing:border-box}
  html,body{width:1200px;height:2251px;overflow:hidden;background:var(--white)}
  body{position:relative;font-family:"Open Sans",Arial,sans-serif;color:var(--ink)}

  .sheet{position:absolute;left:0;width:1200px;height:750px;overflow:hidden;background:var(--white)}
  .sheet--1{top:0}
  .sheet--2{top:751px}
  .sheet--3{top:1501px}

  .idea-band{position:absolute;left:0;top:0;width:1200px;height:61px;background:var(--band);
    display:flex;align-items:center;justify-content:center;font-size:26px;font-weight:400;letter-spacing:.5px;color:var(--ink)}

  .title-block{position:absolute;left:240px;top:74px;width:720px;text-align:center}
  .title-main{font-family:"Archivo",Arial,sans-serif;font-weight:800;font-size:30px;letter-spacing:2px;line-height:34px}
  .title-sub{font-family:"Archivo",Arial,sans-serif;font-weight:700;font-size:15px;color:var(--green);line-height:17px;letter-spacing:.3px}
  .title-tag{font-size:13px;color:#333;line-height:19px;letter-spacing:.3px}

  .brand{position:absolute;left:1010px;top:86px;display:flex;align-items:center;gap:8px}
  .brand-dot{width:18px;height:18px;border-radius:50%;background:var(--green)}
  .brand-name{font-family:"Open Sans",Arial,sans-serif;font-weight:600;font-size:15px;color:var(--green);line-height:18px;width:130px}

  .panel{position:absolute;border:2px solid var(--green);border-radius:8px;background:var(--white)}
  .panel--dark{border-color:var(--ink)}

  .start{left:87px;top:154px;width:291px;height:145px}
  .start-head{position:absolute;left:12px;top:8px;display:flex;align-items:center;gap:9px}
  .start-head svg{width:44px;height:44px}
  .start-title{font-family:"Archivo",Arial,sans-serif;font-weight:600;font-size:14px;line-height:17px;color:var(--grey-text)}
  .dot-list{list-style:none;position:absolute;left:14px;top:56px;font-size:10.5px;line-height:17px;color:var(--ink)}
  .dot-list li{position:relative;padding-left:16px}
  .dot-list li::before{content:"";position:absolute;left:2px;top:6px;width:5px;height:5px;border-radius:50%;background:var(--green)}

  .process{left:400px;top:154px;width:648px;height:145px}
  .process-title{position:absolute;left:0;top:6px;width:100%;text-align:center;font-size:14.5px;color:var(--green);letter-spacing:.3px}
  .process-track{position:absolute;left:68px;top:100px;width:497px;height:2px;background:var(--green)}
  .stage{position:absolute;top:38px;width:100px;margin-left:-50px;text-align:center}
  .stage-icon{width:52px;height:52px;border-radius:50%;background:var(--green-soft);margin:0 auto;display:flex;align-items:center;justify-content:center}
  .stage-icon svg{width:30px;height:30px}
  .stage-dot{width:9px;height:9px;border-radius:50%;background:var(--green);margin:10px auto 0}
  .stage-label{font-size:12.5px;color:var(--green);margin-top:4px}

  .lca{top:309px;height:182px}
  .lca--env{left:87px;width:292px}
  .lca--soc{left:400px;width:314px}
  .lca--cost{left:734px;width:314px}
  .lca-title{position:absolute;left:14px;right:14px;top:9px;text-align:center;font-family:"Archivo",Arial,sans-serif;
    font-weight:600;font-size:13.5px;line-height:17px;padding-bottom:6px;border-bottom:1px solid var(--line);color:var(--grey-text)}
  .lca--soc .lca-title{color:var(--green);border-bottom-color:var(--green)}
  .lca--cost .lca-title{color:var(--ink);border-bottom-color:var(--ink)}
  .lca-icon{position:absolute;left:12px;top:62px;width:62px;height:82px}
  .lca--soc .lca-icon{left:14px;top:70px;width:52px;height:62px}
  .lca--cost .lca-icon{left:10px;top:64px;width:62px;height:80px}
  .bullet-list{list-style:none;position:absolute;top:56px;font-size:10.3px;line-height:12px}
  .lca--env .bullet-list{left:86px;right:6px}
  .lca--soc .bullet-list{left:80px;right:14px}
  .lca--cost .bullet-list{left:78px;right:8px}
  .bullet-list li{position:relative;padding-left:16px;margin-bottom:6px}
  .bullet-list li::before{content:"";position:absolute;left:2px;top:3px;width:4px;height:4px;border-radius:50%;background:var(--ink)}
  .lca--soc .bullet-list li::before{background:var(--green)}

  .connector{position:absolute;border-color:var(--ink);border-style:solid;border-width:0}
  .connector--left{left:232px;top:498px;width:130px;height:34px;border-left-width:1.5px;border-bottom-width:1.5px}
  .connector--right{left:776px;top:498px;width:131px;height:34px;border-right-width:1.5px;border-bottom-width:1.5px}
  .feedback{position:absolute;left:1075px;top:223px;width:38px;height:418px;border:1.5px solid var(--ink);border-left:none}
  .feedback-low{position:absolute;left:920px;top:641px;width:155px;height:0;border-top:1.5px solid var(--ink)}
  .tri{position:absolute;width:0;height:0}
  .tri-right{border-top:7px solid transparent;border-bottom:7px solid transparent;border-left:11px solid var(--ink)}
  .tri-right.green{border-left-color:var(--green)}
  .tri-left{border-top:7px solid transparent;border-bottom:7px solid transparent;border-right:11px solid var(--ink)}
  .tri-down{border-left:6px solid transparent;border-right:6px solid transparent;border-top:9px solid var(--green)}
  .tri-start{left:382px;top:214px;border-top-width:9px;border-bottom-width:9px;border-left-width:14px}
  .tri-left-conn{left:362px;top:525px}
  .tri-right-conn{left:768px;top:525px}
  .tri-feed-top{left:1066px;top:214px;border-top-width:9px;border-bottom-width:9px;border-right-width:14px}
  .tri-feed-low{left:911px;top:632px;border-top-width:9px;border-bottom-width:9px;border-right-width:14px}
  .tri-down-1{left:562px;top:497px}
  .tri-down-2{left:562px;top:571px}

  .balance{left:384px;top:510px;width:368px;height:54px;display:flex;align-items:center;gap:20px;padding-left:34px}
  .balance svg{width:44px;height:44px;flex:none}
  .balance-text{font-family:"Archivo",Arial,sans-serif;font-weight:700;font-size:14px;line-height:18px;color:var(--green);letter-spacing:.3px}

  .benefits{left:241px;top:586px;width:653px;height:108px}
  .benefits-icon{position:absolute;left:28px;top:13px;width:80px;height:80px}
  .benefits-rule{position:absolute;left:139px;top:11px;width:1.5px;height:82px;background:var(--green)}
  .benefits-title{position:absolute;left:175px;top:8px;font-family:"Archivo",Arial,sans-serif;font-weight:700;font-size:13.5px;color:var(--green);letter-spacing:.2px}
  .check-list{list-style:none;position:absolute;top:34px;font-size:10.3px;line-height:12px}
  .check-list--a{left:163px;width:250px}
  .check-list--b{left:414px;width:230px}
  .check-list li{position:relative;padding-left:21px;margin-bottom:6px}
  .check-list--b li{margin-bottom:9px}
  .check-list li svg{position:absolute;left:0;top:0;width:12px;height:12px}

  .footer-line{position:absolute;top:724px;height:1.5px;background:var(--green)}
  .footer-line--a{left:208px;width:184px}
  .footer-line--b{left:808px;width:183px}
  .footer-dot{position:absolute;top:721px;width:7px;height:7px;border-radius:50%;background:var(--green)}
  .footer-dot--a{left:205px}
  .footer-dot--b{left:988px}
  .footer-note{position:absolute;left:402px;top:707px;display:flex;align-items:center;gap:8px;font-size:10.8px;color:var(--green)}
  .footer-note svg{width:36px;height:36px}

  .page-badge{position:absolute;left:1115px;top:686px;width:58px;height:64px;background:var(--green);color:var(--white);
    text-align:center;font-family:"Archivo",Arial,sans-serif;font-weight:700;padding-top:10px}
  .page-badge .label{display:block;font-size:15px;line-height:15px;letter-spacing:.5px}
  .page-badge .num{display:block;font-size:27px;line-height:30px}

  .network-decor{position:absolute;left:860px;top:430px;width:340px;height:320px;
    background:radial-gradient(circle at 65% 55%, rgba(108,138,55,.10), rgba(108,138,55,.04) 55%, rgba(255,255,255,0) 75%)}
  .photo-corner{position:absolute;left:0;top:444px;width:196px;height:306px;
    border-top-right-radius:196px 306px;
    background:linear-gradient(160deg,#c9d3b8 0%,#8e9f74 40%,#5f7641 75%,#43582c 100%)}
  .photo-rim{position:absolute;left:0;top:432px;width:210px;height:318px;border-top-right-radius:210px 318px;background:var(--green-soft)}
</style>
</head>
<body>

<svg width="0" height="0" style="position:absolute" aria-hidden="true">
  <defs>
    <symbol id="i-search" viewBox="0 0 24 24"><circle cx="10" cy="10" r="6.5" fill="none" stroke="#6c8a37" stroke-width="2"/><path d="M15 15l6 6" stroke="#6c8a37" stroke-width="2.4" stroke-linecap="round"/></symbol>
    <symbol id="i-bulb" viewBox="0 0 24 24"><path d="M12 6a5 5 0 0 0-3 9v2.5h6V15a5 5 0 0 0-3-9z" fill="none" stroke="#6c8a37" stroke-width="1.6"/><path d="M9.5 19.5h5M10.5 21.5h3M12 1.5v2M4 9H2M22 9h-2M5.5 3.5l1.4 1.4M18.5 3.5l-1.4 1.4" stroke="#6c8a37" stroke-width="1.5" stroke-linecap="round"/></symbol>
    <symbol id="i-gear" viewBox="0 0 24 24"><path fill="#6c8a37" d="M10.3 1.5h3.4l.5 2.8 1.7.7 2.3-1.6 2.4 2.4-1.6 2.3.7 1.7 2.8.5v3.4l-2.8.5-.7 1.7 1.6 2.3-2.4 2.4-2.3-1.6-1.7.7-.5 2.8h-3.4l-.5-2.8-1.7-.7-2.3 1.6-2.4-2.4 1.6-2.3-.7-1.7-2.8-.5v-3.4l2.8-.5.7-1.7-1.6-2.3 2.4-2.4 2.3 1.6 1.7-.7z"/><circle cx="12" cy="12" r="3.6" fill="#e0e5d6"/></symbol>
    <symbol id="i-cube" viewBox="0 0 24 24"><path d="M12 2.5l8.5 4.8v9.4L12 21.5l-8.5-4.8V7.3z M3.5 7.3L12 12l8.5-4.7M12 12v9.5" fill="none" stroke="#6c8a37" stroke-width="1.5" stroke-linejoin="round"/></symbol>
    <symbol id="i-factory" viewBox="0 0 24 24"><path fill="#6c8a37" d="M2 21V10l6 3.5V10l6 3.5V3h4v7h4v11z"/><rect x="5" y="16" width="2.2" height="2" fill="#e0e5d6"/><rect x="10" y="16" width="2.2" height="2" fill="#e0e5d6"/><rect x="15" y="16" width="2.2" height="2" fill="#e0e5d6"/></symbol>
    <symbol id="i-growth" viewBox="0 0 24 24"><rect x="3" y="15" width="3.5" height="6" fill="#6c8a37"/><rect x="8.5" y="12" width="3.5" height="9" fill="#6c8a37"/><rect x="14" y="9" width="3.5" height="12" fill="#6c8a37"/><path d="M3 11l6-4 4 2 7-6M16 3h4v4" fill="none" stroke="#6c8a37" stroke-width="1.8" stroke-linecap="round" stroke-linejoin="round"/></symbol>
    <symbol id="i-target" viewBox="0 0 48 48"><circle cx="22" cy="26" r="18" fill="none" stroke="#6c8a37" stroke-width="4"/><circle cx="22" cy="26" r="11" fill="none" stroke="#6c8a37" stroke-width="3.5"/><circle cx="22" cy="26" r="4.5" fill="#6c8a37"/><path d="M22 26L40 8" stroke="#6c8a37" stroke-width="3.5" stroke-linecap="round"/><path d="M36 5l7-1-1 7-5 1z" fill="#6c8a37"/></symbol>
    <symbol id="i-globe-leaf" viewBox="0 0 62 82"><circle cx="27" cy="30" r="24" fill="none" stroke="#4a4a4a" stroke-width="3"/><ellipse cx="27" cy="30" rx="10" ry="24" fill="none" stroke="#4a4a4a" stroke-width="2.5"/><path d="M3 30h48M7 18h40M7 42h40M27 6v48" stroke="#4a4a4a" stroke-width="2.5"/><path d="M22 78c2-18 14-30 36-34-2 20-14 32-34 32z" fill="#6c8a37"/><path d="M22 78c8-12 18-22 30-28" stroke="#fff" stroke-width="2" fill="none"/><path d="M20 80c0-10 -6-18-16-20 0 10 6 17 16 20z" fill="#4a4a4a"/></symbol>
    <symbol id="i-people" viewBox="0 0 52 62"><circle cx="26" cy="26" r="24" fill="none" stroke="#6c8a37" stroke-width="2.5"/><circle cx="14" cy="17" r="4.5" fill="#6c8a37"/><circle cx="38" cy="17" r="4.5" fill="#6c8a37"/><circle cx="26" cy="14" r="5.5" fill="#6c8a37"/><path d="M6 33c0-7 4-10 8-10s8 3 8 10zM30 33c0-7 4-10 8-10s8 3 8 10z" fill="#6c8a37"/><path d="M17 33c0-8 4-12 9-12s9 4 9 12z" fill="#4a4a4a"/><path d="M6 46l8-6h8l6 4 6-4h6l6 6-6 6h-4l-8 4-10-6z" fill="#fff" stroke="#4a4a4a" stroke-width="2" stroke-linejoin="round"/></symbol>
    <symbol id="i-euro-chart" viewBox="0 0 62 80"><circle cx="20" cy="20" r="17" fill="none" stroke="#1d1d1b" stroke-width="3"/><text x="20" y="28" text-anchor="middle" font-family="Open Sans, Arial, sans-serif" font-size="22" font-weight="700" fill="#1d1d1b">€</text><rect x="4" y="64" width="8" height="14" fill="#1d1d1b"/><rect x="16" y="56" width="8" height="22" fill="#1d1d1b"/><rect x="28" y="60" width="8" height="18" fill="#1d1d1b"/><rect x="40" y="48" width="8" height="30" fill="#1d1d1b"/><path d="M4 56l14-12 10 6 22-18" fill="none" stroke="#1d1d1b" stroke-width="3"/><path d="M44 30l14-6-4 14z" fill="#6c8a37"/></symbol>
    <symbol id="i-cycle" viewBox="0 0 44 44"><path d="M22 5a17 17 0 0 1 16 12" fill="none" stroke="#1d1d1b" stroke-width="3"/><path d="M39 22a17 17 0 0 1-12 16" fill="none" stroke="#6c8a37" stroke-width="3"/><path d="M22 39A17 17 0 0 1 6 27" fill="none" stroke="#4a4a4a" stroke-width="3"/><path d="M5 22A17 17 0 0 1 15 6" fill="none" stroke="#6c8a37" stroke-width="3"/><path d="M34 14l6 5 1-8z" fill="#1d1d1b"/><path d="M23 35l4 7 5-5z" fill="#6c8a37"/><path d="M10 30l-6-5-1 8z" fill="#4a4a4a"/><path d="M21 9l-4-7-5 5z" fill="#6c8a37"/></symbol>
    <symbol id="i-clipboard" viewBox="0 0 80 80"><circle cx="40" cy="40" r="37" fill="none" stroke="#6c8a37" stroke-width="3"/><rect x="22" y="18" width="34" height="46" rx="4" fill="#fff" stroke="#4a4a4a" stroke-width="2.5"/><rect x="31" y="13" width="16" height="9" rx="2" fill="#6c8a37"/><path d="M27 31l2 2 4-4M27 41l2 2 4-4M27 51l2 2 4-4" fill="none" stroke="#6c8a37" stroke-width="2"/><path d="M37 31h14M37 41h14M37 51h8" stroke="#4a4a4a" stroke-width="2"/><circle cx="56" cy="60" r="11" fill="#6c8a37"/><path d="M50 60l4 4 8-8" fill="none" stroke="#fff" stroke-width="3"/></symbol>
    <symbol id="i-check" viewBox="0 0 12 12"><circle cx="6" cy="6" r="6" fill="#6c8a37"/><path d="M3 6.2l2 2 4-4" fill="none" stroke="#fff" stroke-width="1.5"/></symbol>
    <symbol id="i-globe-small" viewBox="0 0 36 36"><circle cx="18" cy="18" r="16" fill="none" stroke="#6c8a37" stroke-width="1.5"/><circle cx="18" cy="18" r="10" fill="none" stroke="#6c8a37" stroke-width="1.5"/><ellipse cx="18" cy="18" rx="4.5" ry="10" fill="none" stroke="#6c8a37" stroke-width="1.3"/><path d="M8 18h20M10 13h16M10 23h16" stroke="#6c8a37" stroke-width="1.3"/></symbol>
  </defs>
</svg>

<!-- ===== Idea 001 ===== -->
<section class="sheet sheet--1">
  <div class="idea-band">TEMPLATE DESIGN IDEA #001</div>
  <div class="title-block">
    <h1 class="title-main">INTEGRATED PROCESS ASSESSMENT</h1>
    <p class="title-sub">FOR TECHNOLOGY AND PRODUCT INNOVATION</p>
    <p class="title-tag">Ecological, social and economic assessment in early development phases</p>
  </div>
  <div class="brand"><span class="brand-dot"></span><span class="brand-name">Moorwaldinstitut Graz</span></div>

  <div class="panel start">
    <div class="start-head"><svg><use href="#i-target"/></svg><div class="start-title">Starting Point &amp;<br>Methodological Foundations</div></div>
    <ul class="dot-list">
      <li>Products, processes, services and systems</li>
      <li>Market, societal and sustainability requirements</li>
      <li>Goal and scope definition</li>
      <li>Reference system, data basis</li>
      <li>Scenarios and sensitivities</li>
    </ul>
  </div>
  <div class="tri tri-right green tri-start"></div>

  <div class="panel process">
    <div class="process-title">Assessment along the innovation process</div>
    <div class="process-track"></div>
    <div class="stage" style="left:69px"><div class="stage-icon"><svg><use href="#i-search"/></svg></div><div class="stage-dot"></div><div class="stage-label">Research</div></div>
    <div class="stage" style="left:169px"><div class="stage-icon"><svg><use href="#i-bulb"/></svg></div><div class="stage-dot"></div><div class="stage-label">Concept</div></div>
    <div class="stage" style="left:269px"><div class="stage-icon"><svg><use href="#i-gear"/></svg></div><div class="stage-dot"></div><div class="stage-label">Design</div></div>
    <div class="stage" style="left:367px"><div class="stage-icon"><svg><use href="#i-cube"/></svg></div><div class="stage-dot"></div><div class="stage-label">Prototype</div></div>
    <div class="stage" style="left:466px"><div class="stage-icon"><svg><use href="#i-factory"/></svg></div><div class="stage-dot"></div><div class="stage-label">Pilot</div></div>
    <div class="stage" style="left:565px"><div class="stage-icon"><svg><use href="#i-growth"/></svg></div><div class="stage-dot"></div><div class="stage-label">Market uptake</div></div>
  </div>

  <div class="panel lca lca--env">
    <h2 class="lca-title">Environmental Life Cycle<br>Assessment (eLCA)</h2>
    <svg class="lca-icon"><use href="#i-globe-leaf"/></svg>
    <ul class="bullet-list">
      <li>Quantification of environmental impacts and benefits</li>
      <li>Comparison with a reference system</li>
      <li>Carbon footprint and broader impact categories</li>
      <li>ISO 14040/44, accredited models and databases</li>
    </ul>
  </div>
  <div class="panel lca lca--soc">
    <h2 class="lca-title">Social Life Cycle Assessment<br>(S-LCA)</h2>
    <svg class="lca-icon"><use href="#i-people"/></svg>
    <ul class="bullet-list">
      <li>Assessment of social impacts across the life cycle</li>
      <li>Working conditions, health &amp; safety, human rights</li>
      <li>Stakeholder perspective and global value chains</li>
      <li>Social hotspot identification and relevant databases</li>
    </ul>
  </div>
  <div class="panel panel--dark lca lca--cost">
    <h2 class="lca-title">Life Cycle Costing<br>(LCC)</h2>
    <svg class="lca-icon"><use href="#i-euro-chart"/></svg>
    <ul class="bullet-list">
      <li>Economic assessment across the life cycle</li>
      <li>Cost-benefit and techno-economic evaluation</li>
      <li>Infrastructure analyses and market screening</li>
      <li>Roll-out scenarios and cost drivers</li>
    </ul>
  </div>

  <div class="tri tri-down tri-down-1"></div>
  <div class="connector connector--left"></div><div class="tri tri-right tri-left-conn"></div>
  <div class="connector connector--right"></div><div class="tri tri-left tri-right-conn"></div>
  <div class="panel balance"><svg><use href="#i-cycle"/></svg><div class="balance-text">Balancing ecology, social aspects<br>and economy</div></div>
  <div class="tri tri-down tri-down-2"></div>

  <div class="feedback"></div><div class="feedback-low"></div>
  <div class="tri tri-left tri-feed-top"></div><div class="tri tri-left tri-feed-low"></div>

  <div class="panel benefits">
    <svg class="benefits-icon"><use href="#i-clipboard"/></svg>
    <div class="benefits-rule"></div>
    <h3 class="benefits-title">Integrated Process Assessment – Concrete Benefits</h3>
    <ul class="check-list check-list--a">
      <li><svg><use href="#i-check"/></svg>Early identification of opportunities and risks</li>
      <li><svg><use href="#i-check"/></svg>Sound decision support</li>
      <li><svg><use href="#i-check"/></svg>Comparison of technologies and product options</li>
    </ul>
    <ul class="check-list check-list--b">
      <li><svg><use href="#i-check"/></svg>Iterative feedback for development decisions</li>
      <li><svg><use href="#i-check"/></svg>Holistic view of ecological, social and economic performance</li>
    </ul>
  </div>

  <div class="footer-dot footer-dot--a"></div><div class="footer-line footer-line--a"></div>
  <div class="footer-note"><svg><use href="#i-globe-small"/></svg>Broadly applicable to diverse technologies, processes and products</div>
  <div class="footer-line footer-line--b"></div><div class="footer-dot footer-dot--b"></div>
  <div class="page-badge"><span class="label">PAGE</span><span class="num">01</span></div>
</section>

<!-- ===== Idea 002 ===== -->
<section class="sheet sheet--2">
  <div class="network-decor" role="img" aria-label="Faint network of connected nodes as background decoration"></div>
  <div class="idea-band">TEMPLATE DESIGN IDEA #002</div>
  <div class="title-block">
    <h1 class="title-main">INTEGRATED PROCESS ASSESSMENT</h1>
    <p class="title-sub">FOR TECHNOLOGY AND PRODUCT INNOVATION</p>
    <p class="title-tag">Ecological, social and economic assessment in early development phases</p>
  </div>
  <div class="brand"><span class="brand-dot"></span><span class="brand-name">Moorwaldinstitut Graz</span></div>

  <div class="panel start">
    <div class="start-head"><svg><use href="#i-target"/></svg><div class="start-title">Starting Point &amp;<br>Methodological Foundations</div></div>
    <ul class="dot-list">
      <li>Products, processes, services and systems</li>
      <li>Market, societal and sustainability requirements</li>
      <li>Goal and scope definition</li>
      <li>Reference system, data basis</li>
      <li>Scenarios and sensitivities</li>
    </ul>
  </div>
  <div class="tri tri-right green tri-start"></div>

  <div class="panel process">
    <div class="process-title">Assessment along the innovation process</div>
    <div class="process-track"></div>
    <div class="stage" style="left:69px"><div class="stage-icon"><svg><use href="#i-search"/></svg></div><div class="stage-dot"></div><div class="stage-label">Research</div></div>
    <div class="stage" style="left:169px"><div class="stage-icon"><svg><use href="#i-bulb"/></svg></div><div class="stage-dot"></div><div class="stage-label">Concept</div></div>
    <div class="stage" style="left:269px"><div class="stage-icon"><svg><use href="#i-gear"/></svg></div><div class="stage-dot"></div><div class="stage-label">Design</div></div>
    <div class="stage" style="left:367px"><div class="stage-icon"><svg><use href="#i-cube"/></svg></div><div class="stage-dot"></div><div class="stage-label">Prototype</div></div>
    <div class="stage" style="left:466px"><div class="stage-icon"><svg><use href="#i-factory"/></svg></div><div class="stage-dot"></div><div class="stage-label">Pilot</div></div>
    <div class="stage" style="left:565px"><div class="stage-icon"><svg><use href="#i-growth"/></svg></div><div class="stage-dot"></div><div class="stage-label">Market uptake</div></div>
  </div>

  <div class="panel lca lca--env">
    <h2 class="lca-title">Environmental Life Cycle<br>Assessment (eLCA)</h2>
    <svg class="lca-icon"><use href="#i-globe-leaf"/></svg>
    <ul class="bullet-list">
      <li>Quantification of environmental impacts and benefits</li>
      <li>Comparison with a reference system</li>
      <li>Carbon footprint and broader impact categories</li>
      <li>ISO 14040/44, accredited models and databases</li>
    </ul>
  </div>
  <div class="panel lca lca--soc">
    <h2 class="lca-title">Social Life Cycle Assessment<br>(S-LCA)</h2>
    <svg class="lca-icon"><use href="#i-people"/></svg>
    <ul class="bullet-list">
      <li>Assessment of social impacts across the life cycle</li>
      <li>Working conditions, health &amp; safety, human rights</li>
      <li>Stakeholder perspective and global value chains</li>
      <li>Social hotspot identification and relevant databases</li>
    </ul>
  </div>
  <div class="panel panel--dark lca lca--cost">
    <h2 class="lca-title">Life Cycle Costing<br>(LCC)</h2>
    <svg class="lca-icon"><use href="#i-euro-chart"/></svg>
    <ul class="bullet-list">
      <li>Economic assessment across the life cycle</li>
      <li>Cost-benefit and techno-economic evaluation</li>
      <li>Infrastructure analyses and market screening</li>
      <li>Roll-out scenarios and cost drivers</li>
    </ul>
  </div>

  <div class="tri tri-down tri-down-1"></div>
  <div class="connector connector--left"></div><div class="tri tri-right tri-left-conn"></div>
  <div class="connector connector--right"></div><div class="tri tri-left tri-right-conn"></div>
  <div class="panel balance"><svg><use href="#i-cycle"/></svg><div class="balance-text">Balancing ecology, social aspects<br>and economy</div></div>
  <div class="tri tri-down tri-down-2"></div>

  <div class="feedback"></div><div class="feedback-low"></div>
  <div class="tri tri-left tri-feed-top"></div><div class="tri tri-left tri-feed-low"></div>

  <div class="panel benefits">
    <svg class="benefits-icon"><use href="#i-clipboard"/></svg>
    <div class="benefits-rule"></div>
    <h3 class="benefits-title">Integrated Process Assessment – Concrete Benefits</h3>
    <ul class="check-list check-list--a">
      <li><svg><use href="#i-check"/></svg>Early identification of opportunities and risks</li>
      <li><svg><use href="#i-check"/></svg>Sound decision support</li>
      <li><svg><use href="#i-check"/></svg>Comparison of technologies and product options</li>
    </ul>
    <ul class="check-list check-list--b">
      <li><svg><use href="#i-check"/></svg>Iterative feedback for development decisions</li>
      <li><svg><use href="#i-check"/></svg>Holistic view of ecological, social and economic performance</li>
    </ul>
  </div>

  <div class="footer-dot footer-dot--a"></div><div class="footer-line footer-line--a"></div>
  <div class="footer-note"><svg><use href="#i-globe-small"/></svg>Broadly applicable to diverse technologies, processes and products</div>
  <div class="footer-line footer-line--b"></div><div class="footer-dot footer-dot--b"></div>
  <div class="page-badge"><span class="label">PAGE</span><span class="num">01</span></div>
</section>

<!-- ===== Idea 003 ===== -->
<section class="sheet sheet--3">
  <div class="network-decor" role="img" aria-label="Faint network of connected nodes as background decoration"></div>
  <div class="photo-rim"></div>
  <div class="photo-corner" role="img" aria-label="Photo of a modern building surrounded by green trees"></div>
  <div class="idea-band">TEMPLATE DESIGN IDEA #003</div>
  <div class="title-block">
    <h1 class="title-main">INTEGRATED PROCESS ASSESSMENT</h1>
    <p class="title-sub">FOR TECHNOLOGY AND PRODUCT INNOVATION</p>
    <p class="title-tag">Ecological, social and economic assessment in early development phases</p>
  </div>
  <div class="brand"><span class="brand-dot"></span><span class="brand-name">Moorwaldinstitut Graz</span></div>

  <div class="panel start">
    <div class="start-head"><svg><use href="#i-target"/></svg><div class="start-title">Starting Point &amp;<br>Methodological Foundations</div></div>
    <ul class="dot-list">
      <li>Products, processes, services and systems</li>
      <li>Market, societal and sustainability requirements</li>
      <li>Goal and scope definition</li>
      <li>Reference system, data basis</li>
      <li>Scenarios and sensitivities</li>
    </ul>
  </div>
  <div class="tri tri-right green tri-start"></div>

  <div class="panel process">
    <div class="process-title">Assessment along the innovation process</div>
    <div class="process-track"></div>
    <div class="stage" style="left:69px"><div class="stage-icon"><svg><use href="#i-search"/></svg></div><div class="stage-dot"></div><div class="stage-label">Research</div></div>
    <div class="stage" style="left:169px"><div class="stage-icon"><svg><use href="#i-bulb"/></svg></div><div class="stage-dot"></div><div class="stage-label">Concept</div></div>
    <div class="stage" style="left:269px"><div class="stage-icon"><svg><use href="#i-gear"/></svg></div><div class="stage-dot"></div><div class="stage-label">Design</div></div>
    <div class="stage" style="left:367px"><div class="stage-icon"><svg><use href="#i-cube"/></svg></div><div class="stage-dot"></div><div class="stage-label">Prototype</div></div>
    <div class="stage" style="left:466px"><div class="stage-icon"><svg><use href="#i-factory"/></svg></div><div class="stage-dot"></div><div class="stage-label">Pilot</div></div>
    <div class="stage" style="left:565px"><div class="stage-icon"><svg><use href="#i-growth"/></svg></div><div class="stage-dot"></div><div class="stage-label">Market uptake</div></div>
  </div>

  <div class="panel lca lca--env">
    <h2 class="lca-title">Environmental Life Cycle<br>Assessment (eLCA)</h2>
    <svg class="lca-icon"><use href="#i-globe-leaf"/></svg>
    <ul class="bullet-list">
      <li>Quantification of environmental impacts and benefits</li>
      <li>Comparison with a reference system</li>
      <li>Carbon footprint and broader impact categories</li>
      <li>ISO 14040/44, accredited models and databases</li>
    </ul>
  </div>
  <div class="panel lca lca--soc">
    <h2 class="lca-title">Social Life Cycle Assessment<br>(S-LCA)</h2>
    <svg class="lca-icon"><use href="#i-people"/></svg>
    <ul class="bullet-list">
      <li>Assessment of social impacts across the life cycle</li>
      <li>Working conditions, health &amp; safety, human rights</li>
      <li>Stakeholder perspective and global value chains</li>
      <li>Social hotspot identification and relevant databases</li>
    </ul>
  </div>
  <div class="panel panel--dark lca lca--cost">
    <h2 class="lca-title">Life Cycle Costing<br>(LCC)</h2>
    <svg class="lca-icon"><use href="#i-euro-chart"/></svg>
    <ul class="bullet-list">
      <li>Economic assessment across the life cycle</li>
      <li>Cost-benefit and techno-economic evaluation</li>
      <li>Infrastructure analyses and market screening</li>
      <li>Roll-out scenarios and cost drivers</li>
    </ul>
  </div>

  <div class="tri tri-down tri-down-1"></div>
  <div class="connector connector--left"></div><div class="tri tri-right tri-left-conn"></div>
  <div class="connector connector--right"></div><div class="tri tri-left tri-right-conn"></div>
  <div class="panel balance"><svg><use href="#i-cycle"/></svg><div class="balance-text">Balancing ecology, social aspects<br>and economy</div></div>
  <div class="tri tri-down tri-down-2"></div>

  <div class="feedback"></div><div class="feedback-low"></div>
  <div class="tri tri-left tri-feed-top"></div><div class="tri tri-left tri-feed-low"></div>

  <div class="panel benefits">
    <svg class="benefits-icon"><use href="#i-clipboard"/></svg>
    <div class="benefits-rule"></div>
    <h3 class="benefits-title">Integrated Process Assessment – Concrete Benefits</h3>
    <ul class="check-list check-list--a">
      <li><svg><use href="#i-check"/></svg>Early identification of opportunities and risks</li>
      <li><svg><use href="#i-check"/></svg>Sound decision support</li>
      <li><svg><use href="#i-check"/></svg>Comparison of technologies and product options</li>
    </ul>
    <ul class="check-list check-list--b">
      <li><svg><use href="#i-check"/></svg>Iterative feedback for development decisions</li>
      <li><svg><use href="#i-check"/></svg>Holistic view of ecological, social and economic performance</li>
    </ul>
  </div>

  <div class="footer-dot footer-dot--a"></div><div class="footer-line footer-line--a"></div>
  <div class="footer-note"><svg><use href="#i-globe-small"/></svg>Broadly applicable to diverse technologies, processes and products</div>
  <div class="footer-line footer-line--b"></div><div class="footer-dot footer-dot--b"></div>
  <div class="page-badge"><span class="label">PAGE</span><span class="num">01</span></div>
</section>

</body>
</html>
```